Marrowby Cay Soda

We need an eco-label designed to go on our soda bottles that will be for sale on a tiny island off the east coast of Australia. The label is a printed card (double sided) that is 60mm wide and 180mm long. There is a 40mm by 40mm hole that is used to place on the bottle, as shown in the photos. One side is the back label, this has some regulatory requirements such as a panel of % of dietary intake, an ingredient list and a line that reads "Batch:_________". That is standard on each back panel. The front needs to have the name of the soda flavour and design of label. The reverse will need to have a blurb about us, our story and how to recycle the bottle.

We would like the design to be funny, possibly using Commodore Sir Basil Tranter's photoshopped image (he is a grizzly dude the island is named after see google images) or anything you talented people come up with.

We want to use the same format and then will need to change the name for the flavours, change the ingredients list and replace the standard box for the % daily intake.

Target Market(s)

The Product will stand next to the big soda companies that all know and thus must stand out visually from them to get the customer to have a second look at the product

Industry/Entity Type

Soda

Requirements
Must have
• Space for the Flavour on the front ie "Lemonade". "Batch:_________" at the base of the back panel.
Nice to have
• Island feel, Possibly using "Commodore Sir Tranter" holding a drink?!? Palms, sunsets

```html
<!DOCTYPE html>
<html lang="en">
<head>
<meta charset="utf-8">
<title>Marrowby Cay Soda – Bottle Tag</title>
<link href="https://fonts.googleapis.com/css2?family=Lilita+One&family=Open+Sans:wght@400;700;800&display=swap" rel="stylesheet">
<style>
  :root {
    --paper: #ffffff;
    --sand: #f3d27a;
    --sand-light: #f8e3a6;
    --tangerine: #d9822b;
    --tangerine-light: #e49a4c;
    --navy: #2b3568;
    --ink: #1d1d1d;
    --white: #ffffff;
    --skin: #f0a9a3;
    --sun: #f5c842;
    --sky: #f7efe0;
  }
  * { box-sizing: border-box; margin: 0; padding: 0; }
  html, body { width: 902px; height: 1200px; overflow: hidden; background: var(--paper); }
  .canvas { position: relative; width: 902px; height: 1200px; }

  .tag {
    position: absolute;
    top: 87px;
    width: 383px;
    height: 1055px;
    border-radius: 40px;
    overflow: hidden;
  }
  .tag--back  { left: 62px;  background: radial-gradient(ellipse at 40% 45%, var(--sand-light), var(--sand) 70%); }
  .tag--story { left: 492px; width: 352px; background: radial-gradient(ellipse at 50% 50%, var(--tangerine-light), var(--tangerine) 70%); }

  .bottle-hole {
    position: absolute;
    width: 216px; height: 216px;
    border-radius: 50%;
    border: 2px dashed var(--ink);
  }
  .tag--back .bottle-hole  { left: 84px; top: 405px; }
  .tag--story .bottle-hole { left: 63px; top: 408px; border-color: #6b3a10; }

  /* Regulatory panel (printed upside down) */
  .regulatory {
    position: absolute;
    left: 58px; top: 16px;
    width: 258px;
    transform: rotate(180deg);
    font-family: "Open Sans", sans-serif;
    color: var(--ink);
  }
  .nutrition {
    background: var(--white);
    border: 2px solid var(--ink);
    padding: 5px 7px;
    font-size: 9px;
    line-height: 1.35;
  }
  .nutrition__title { font-size: 22px; font-weight: 800; line-height: 1; letter-spacing: -0.3px; }
  .nutrition__row { display: flex; justify-content: space-between; border-top: 1px solid var(--ink); padding: 1px 0; }
  .nutrition__row--thick { border-top: 6px solid var(--ink); }
  .nutrition__row--mid { border-top: 3px solid var(--ink); }
  .nutrition__row--indent { padding-left: 10px; }
  .nutrition__note { border-top: 3px solid var(--ink); padding-top: 2px; font-size: 8px; }
  .ingredients { margin-top: 8px; font-size: 8px; line-height: 1.3; font-weight: 700; }

  /* Front */
  .brand {
    position: absolute;
    left: 0; right: 0; top: 700px;
    text-align: center;
    font-family: "Lilita One", sans-serif;
    font-size: 46px;
    line-height: 0.95;
    color: var(--navy);
    letter-spacing: 0.5px;
  }
  .mascot-scene {
    position: absolute;
    left: 0; right: 0; bottom: 0;
    height: 312px;
    background:
      radial-gradient(circle at 76% 22%, var(--sky) 0 52px, transparent 53px),
      radial-gradient(ellipse at 28% 70%, var(--skin) 0 38%, transparent 62%),
      linear-gradient(180deg, transparent 0%, var(--sun) 70%, #8fc3b5 100%);
  }
  .flavour {
    position: absolute;
    left: 204px; top: 938px;
    width: 140px;
    padding: 6px 0;
    background: var(--sun);
    border: 2px solid var(--navy);
    transform: rotate(-8deg);
    text-align: center;
    font-family: "Open Sans", sans-serif;
    font-weight: 800;
    font-size: 20px;
    color: var(--navy);
  }

  /* Story side */
  .portrait {
    position: absolute;
    left: 38px; top: 41px;
    width: 124px; height: 124px;
    border-radius: 50%;
    background: radial-gradient(circle at 50% 60%, var(--skin), var(--sun) 70%);
    border: 3px solid var(--white);
  }
  .heading {
    font-family: "Lilita One", sans-serif;
    color: var(--white);
    line-height: 0.95;
    letter-spacing: 1px;
  }
  .heading--story {
    position: absolute;
    left: 186px; top: 118px;
    font-size: 50px;
    text-align: center;
  }
  .heading--recycle {
    position: absolute;
    left: 38px; top: 706px;
    font-size: 34px;
  }
  .copy {
    position: absolute;
    left: 38px;
    width: 278px;
    font-family: "Open Sans", sans-serif;
    font-weight: 700;
    font-size: 16.5px;
    line-height: 21.7px;
    color: var(--white);
  }
  .copy--story   { top: 228px; }
  .copy--recycle { top: 765px; }
  .palm-corner {
    position: absolute;
    right: 0; bottom: 0;
    width: 90px; height: 80px;
    background: radial-gradient(ellipse at 70% 80%, rgba(245,200,120,0.55), transparent 70%);
  }
</style>
</head>
<body>
<main class="canvas">

  <section class="tag tag--back" aria-label="Front and back label">
    <div class="regulatory">
      <div class="nutrition">
        <div class="nutrition__title">Nutrition Facts</div>
        <div>Serving Size 1 Bottle (355 mL)</div>
        <div class="nutrition__row nutrition__row--thick"><span>Amount Per Serving</span></div>
        <div class="nutrition__row"><strong>Calories 160</strong></div>
        <div class="nutrition__row nutrition__row--mid"><span></span><strong>% Daily Value*</strong></div>
        <div class="nutrition__row"><span><strong>Total Fat</strong> 0g</span><strong>0%</strong></div>
        <div class="nutrition__row"><span><strong>Sodium</strong> 15mg</span><strong>1%</strong></div>
        <div class="nutrition__row"><span><strong>Total Carbohydrate</strong> 42g</span><strong>14%</strong></div>
        <div class="nutrition__row nutrition__row--indent"><span>Sugars 42g</span></div>
        <div class="nutrition__row"><span><strong>Protein</strong> 0g</span></div>
        <div class="nutrition__note">*Percent Daily Values are based on a 2,000 calorie diet.</div>
      </div>
      <p class="ingredients">Ingredients: carbonated water, cane sugar, lemon juice, natural lemon flavour, citric acid. Batch:_________ Best served cold.</p>
    </div>

    <div class="bottle-hole" aria-hidden="true"></div>

    <h1 class="brand">Marrowby Cay<br>Soda</h1>

    <div class="mascot-scene" role="img" aria-label="Cartoon of Commodore Sir Tranter in sunglasses raising a glass of soda, with a pale sun and palm trees"></div>
    <div class="flavour">Lemonade</div>
  </section>

  <section class="tag tag--story" aria-label="Our story and recycling side">
    <div class="portrait" role="img" aria-label="Cartoon portrait of Commodore Sir Tranter in sunglasses"></div>
    <h2 class="heading heading--story">OUR<br>STORY</h2>
    <p class="copy copy--story">Lorem ipsum dolor sit amet, consectetur adipiscing elit, sed do eiusmod tempor incididunt ut labore et dolore magna aliqua. Ut enim ad minim veniam, quis nostrud exercitation ullamco laboris nisi ut aliquip ex ea commodo consequat.</p>

    <div class="bottle-hole" aria-hidden="true"></div>

    <h2 class="heading heading--recycle">HOW TO RECYCLE</h2>
    <p class="copy copy--recycle">Lorem ipsum dolor sit amet, consectetur adipiscing elit, sed do eiusmod tempor incididunt ut labore et dolore magna aliqua. Ut enim ad minim veniam, quis nostrud exercitation ullamco laboris nisi ut aliquip ex ea commodo consequat. Lorem ipsum dolor sit amet, consectetur adipiscing elit, sed do eiusmod tempor incididunt ut</p>
    <div class="palm-corner" role="img" aria-label="Pale palm tree silhouettes"></div>
  </section>

</main>
</body>
</html>
```